Summit body trim co

We want a yard sign designed people can read from inside their cars. 24"x18". We are a start up business in Minneapolis Mn. We are the FAT LOSS place. We guarantee 25-45+lbs. of fat loss in 40 days. Because of our technology. Its Doctor supervised for safety and results. WWW.summitbodytrimCo.com

Industry/Entity Type

Business

```html
<!DOCTYPE html>
<html lang="en">
<head>
<meta charset="utf-8">
<title>Summit body trim co — Fat Loss Yard Sign</title>
<link rel="stylesheet" href="https://fonts.googleapis.com/css2?family=Alfa+Slab+One&family=Open+Sans:wght@400;600;700&family=Fira+Sans+Condensed:wght@600&display=swap">
<style>
  :root {
    --green: #8dc63f;
    --purple: #6a3787;
    --orange: #f7941d;
    --red: #be1e2d;
    --ink: #111111;
    --paper: #ffffff;
    --frame: #b9b9b9;
  }
  * { margin: 0; padding: 0; box-sizing: border-box; }
  html, body { width: 900px; height: 1200px; overflow: hidden; background: var(--paper); }
  .sign { position: relative; width: 900px; height: 1200px; overflow: hidden; }
  .sign-frame { position: absolute; left: 15px; top: 15px; width: 870px; height: 1170px; border: 1px solid var(--frame); pointer-events: none; z-index: 5; }
  .backdrop { position: absolute; left: 15px; top: 15px; width: 870px; height: 1170px; }
  .slab { font-family: "Alfa Slab One", "Rockwell", serif; color: var(--ink); position: absolute; line-height: 1; white-space: nowrap; z-index: 2; }
  .headline { left: 0; width: 900px; top: 40px; text-align: center; font-size: 118px; letter-spacing: 10px; padding-left: 10px; }
  .guarantee-stroke { position: absolute; left: 488px; top: 212px; width: 355px; height: 125px; }
  .guarantee { left: 448px; top: 192px; font-size: 46px; transform: rotate(-6deg); transform-origin: left bottom; }
  .figure-art { position: absolute; left: 20px; top: 165px; width: 290px; height: 870px; z-index: 1;
    background: linear-gradient(180deg, #f6b63a 0%, #9bcf45 20%, #9bcf45 37%, #8e47a3 50%, #8e47a3 74%, #f2b27c 88%, #8cc63f 100%);
    border-radius: 140px 140px 50px 50px; opacity: .85; }
  .offer-lose { left: 430px; top: 434px; font-size: 92px; letter-spacing: 4px; }
  .offer-amount { left: 325px; top: 524px; font-size: 92px; letter-spacing: 1px; color: var(--purple); }
  .offer-of { position: absolute; left: 818px; top: 524px; font-family: "Open Sans", sans-serif; font-size: 26px; color: var(--ink); }
  .offer-fat { left: 325px; top: 618px; font-size: 92px; letter-spacing: 7px; }
  .offer-in { position: absolute; left: 352px; top: 748px; font-family: "Open Sans", sans-serif; font-size: 26px; color: var(--ink); }
  .offer-days { left: 392px; top: 706px; font-size: 92px; }
  .tech-bar { position: absolute; left: 323px; top: 810px; width: 562px; height: 48px; background: var(--ink); color: var(--paper); z-index: 2;
    font-family: "Open Sans", sans-serif; font-size: 30px; line-height: 48px; padding-left: 60px; }
  .supervision { position: absolute; left: 490px; top: 878px; width: 375px; text-align: center; font-family: "Open Sans", sans-serif; font-size: 29px; line-height: 40px; color: var(--ink); }
  .cta-arrow { position: absolute; left: 15px; top: 1014px; width: 427px; height: 82px; z-index: 2; }
  .cta-label { position: absolute; left: 66px; top: 1030px; font-family: "Open Sans", sans-serif; font-weight: 700; font-size: 44px; line-height: 1.1; color: var(--paper); z-index: 3; }
  .phone { position: absolute; left: 452px; top: 1004px; font-family: "Fira Sans Condensed", "Arial Narrow", sans-serif; font-weight: 600; font-size: 72px; color: var(--ink); letter-spacing: 1px; }
  .web-band { position: absolute; left: 15px; top: 1096px; width: 870px; height: 89px; background: var(--purple); color: var(--paper);
    font-family: "Open Sans", sans-serif; font-size: 62px; line-height: 89px; text-align: center; letter-spacing: 1px; }
</style>
</head>
<body>
<main class="sign">
  <svg class="backdrop" viewBox="0 0 870 1170" aria-hidden="true">
    <path d="M0 0 H870 V165 C620 195 180 360 0 745 Z" fill="var(--green)"/>
  </svg>

  <h1 class="slab headline">FAT LOSS</h1>

  <div class="figure-art" role="img" aria-label="Illustration of a fit woman in workout clothes holding an apple, wrapped in a measuring tape"></div>

  <svg class="guarantee-stroke" viewBox="0 0 355 125" role="img" aria-label="Red brush stroke underline">
    <path d="M8 118 L330 10 L345 24 L120 88 L250 70 L30 124 Z" fill="var(--red)"/>
  </svg>
  <p class="slab guarantee">GUARANTEED!</p>

  <p class="slab offer-lose">LOSE</p>
  <p class="slab offer-amount">25-45+lbs.</p><span class="offer-of">of</span>
  <p class="slab offer-fat">FAT LOSS</p>
  <span class="offer-in">in</span><p class="slab offer-days">40 days</p>

  <p class="tech-bar">Because of our technology</p>
  <p class="supervision">Doctor supervised<br>for safety and results</p>

  <svg class="cta-arrow" viewBox="0 0 427 82" aria-hidden="true">
    <path d="M0 14 H345 V0 L427 41 L345 82 V68 H0 Z" fill="var(--orange)"/>
  </svg>
  <p class="cta-label">START NOW!</p>
  <p class="phone">612-555-0148</p>

  <p class="web-band">summitbodytrimco.com</p>
  <div class="sign-frame"></div>
</main>
</body>
</html>
```